Create a new business card

I’m looking to update my business card to make it match the rest of my brand. I will include my current website as well as what my vehicle designs look like, etc..
What my business currently services
Weekly maintenance pool openings / closings
Equipment repair, including pumps, heaters, salt systems, filters, etc.
We install automatic covers and maintain them as well as provide preventative maintenance

I would like to include my name.
Darren Holcott.
My title
Owner
My email
Darren@tidewellnx.com
4015867120
Www.tidewellnx.com

```html
<!DOCTYPE html>
<html lang="en">
<head>
<meta charset="utf-8">
<title>Tidewell Pool Service – Business Card</title>
<link rel="stylesheet" href="https://fonts.googleapis.com/css2?family=Montserrat:wght@400;500;600&display=swap">
<style>
  :root {
    --navy: #212b5c;
    --navy-soft: #2c3873;
    --sky: #29a3e0;
    --orange: #ec6a1f;
    --ink: #2a2a2e;
    --paper: #ffffff;
    --paper-shade: #f1f2f4;
    --stage: #dcdde0;
  }
  * { box-sizing: border-box; margin: 0; padding: 0; }
  html, body {
    width: 1200px; height: 1200px; overflow: hidden;
    background: var(--stage);
    font-family: "Montserrat", sans-serif;
  }
  .sheet {
    width: 1200px; height: 1200px;
    display: flex; flex-direction: column; align-items: center; justify-content: center;
    gap: 60px;
  }
  .card {
    position: relative;
    width: 900px; height: 514px;
    border-radius: 34px;
    overflow: hidden;
    box-shadow: 0 10px 30px rgba(0,0,0,0.18);
  }
  /* Front */
  .card-front { background: linear-gradient(180deg, var(--paper) 0%, var(--paper-shade) 100%); }
  .card-front .wave { position: absolute; inset: 0; width: 100%; height: 100%; }
  .identity {
    position: absolute; left: 80px; top: 150px;
    border-left: 7px solid var(--sky);
    padding-left: 14px;
  }
  .identity .name {
    color: var(--sky); font-weight: 500; font-size: 40px;
    letter-spacing: 1px; text-transform: uppercase; line-height: 1;
  }
  .identity .title {
    color: var(--ink); font-weight: 400; font-size: 26px;
    text-transform: uppercase; line-height: 1.1; margin-top: 4px;
  }
  .contacts {
    position: absolute; left: 110px; top: 268px;
    list-style: none;
  }
  .contacts li {
    display: flex; align-items: center; gap: 16px;
    color: var(--ink); font-size: 27px; font-weight: 400;
    height: 42px;
  }
  .contacts svg { width: 28px; height: 28px; flex: none; }
  .brand {
    position: absolute; display: flex; align-items: center; gap: 18px;
  }
  .brand .dot { border-radius: 50%; flex: none; }
  .brand .brand-name { font-weight: 600; line-height: 1.05; }
  .card-front .brand { right: 60px; top: 70px; }
  .card-front .brand .dot { width: 70px; height: 70px; background: var(--sky); }
  .card-front .brand .brand-name { color: var(--navy); font-size: 34px; }
  /* Back */
  .card-back {
    background: radial-gradient(circle at 50% 50%, var(--navy-soft) 0%, var(--navy) 70%);
  }
  .card-back .brand {
    left: 50%; top: 50%; transform: translate(-50%, -50%);
  }
  .card-back .brand .dot { width: 110px; height: 110px; background: var(--sky); }
  .card-back .brand .brand-name { color: var(--paper); font-size: 52px; }
</style>
</head>
<body>
<main class="sheet">
  <section class="card card-front" aria-label="Business card front">
    <svg class="wave" viewBox="0 0 900 514" preserveAspectRatio="none" aria-hidden="true">
      <path d="M0 470 C 260 440, 640 400, 820 300 C 870 270, 895 230, 900 180" fill="none" stroke="var(--orange)" stroke-width="9"/>
      <path d="M0 514 L0 488 C 260 462, 660 420, 840 320 C 880 296, 898 262, 900 230 L900 514 Z" fill="var(--navy)"/>
    </svg>

    <div class="brand">
      <span class="dot"></span>
      <span class="brand-name">Tidewell<br>Pool Service</span>
    </div>

    <div class="identity">
      <p class="name">Darren Holcott</p>
      <p class="title">Owner</p>
    </div>

    <ul class="contacts">
      <li>
        <svg viewBox="0 0 24 24" aria-hidden="true"><path fill="var(--sky)" d="M6.6 10.8a15.1 15.1 0 0 0 6.6 6.6l2.2-2.2a1 1 0 0 1 1-.25 11.4 11.4 0 0 0 3.6.57 1 1 0 0 1 1 1V20a1 1 0 0 1-1 1A17 17 0 0 1 3 4a1 1 0 0 1 1-1h3.5a1 1 0 0 1 1 1c0 1.25.2 2.45.57 3.57a1 1 0 0 1-.25 1z"/></svg>
        <span>(401) 586-7120</span>
      </li>
      <li>
        <svg viewBox="0 0 24 24" aria-hidden="true"><rect x="2" y="5" width="20" height="14" rx="1.5" fill="var(--sky)"/><path d="M3 6.5l9 7 9-7" fill="none" stroke="#fff" stroke-width="1.6"/></svg>
        <span>Darren@tidewellnx.com</span>
      </li>
      <li>
        <svg viewBox="0 0 24 24" aria-hidden="true"><g fill="none" stroke="var(--sky)" stroke-width="1.8"><circle cx="12" cy="12" r="9.5"/><ellipse cx="12" cy="12" rx="4.2" ry="9.5"/><path d="M2.5 12h19M4 7h16M4 17h16"/></g></svg>
        <span>www.tidewellnx.com</span>
      </li>
    </ul>
  </section>

  <section class="card card-back" aria-label="Business card back">
    <div class="brand">
      <span class="dot"></span>
      <span class="brand-name">Tidewell<br>Pool Service</span>
    </div>
  </section>
</main>
</body>
</html>
```